Stationery Set for new venture capital firm

We need a new set of stationery including letterhead, business cards, envelopes, with compliment slips for our new startup venture capital firm known as Halvora.
We make alternative investments globally and hope to have a worldwide network of offices later.

The stationery should be elegant and not too fussy with the use of too many colors.

Venture Capital

```html
<!DOCTYPE html>
<html lang="en">
<head>
<meta charset="utf-8">
<title>Halvora Stationery Set</title>
<link rel="stylesheet" href="https://fonts.googleapis.com/css2?family=Tinos:wght@400;700&display=swap">
<style>
:root{
  --stage:#6b4a30;
  --paper:#ffffff;
  --paper-shade:#f1f1f1;
  --brand-blue:#1e9ad6;
  --swoop-grey:#8a8a8a;
  --ink:#333333;
  --ink-soft:#666666;
  --card-dark:#2b2b2b;
  --card-grey:#6e6e6e;
  --label:#ffffff;
}
*{margin:0;padding:0;box-sizing:border-box}
html,body{width:1200px;height:517px;overflow:hidden}
body{background:var(--stage);font-family:"Tinos",serif;color:var(--ink);position:relative}
.sheet{position:absolute;background:var(--paper);overflow:hidden;box-shadow:0 2px 6px rgba(0,0,0,.35)}
.swoop{position:absolute;top:0;right:0}
.brand{position:absolute;display:flex;align-items:center;gap:6px;font-family:"Tinos",serif;font-weight:700;color:var(--brand-blue)}
.brand-dot{border-radius:50%;background:var(--brand-blue);flex:none}
.header-address{position:absolute;color:var(--paper);font-size:8.5px;line-height:10px}
.contact-list{position:absolute;font-size:6.5px;line-height:8px;list-style:none;color:var(--ink)}
.contact-list li{display:flex;align-items:center;gap:4px}
.contact-list svg{width:6px;height:6px;fill:var(--ink)}

/* letterhead */
.letterhead-a{left:14px;top:16px;width:338px;height:422px}
.letterhead-b{left:376px;top:16px;width:339px;height:422px}
.fax-title{position:absolute;left:12px;top:124px;font-size:21px;letter-spacing:.5px}
.fax-fields{position:absolute;left:12px;top:160px;width:289px}
.fax-row{display:flex;height:17px;border-bottom:1px solid var(--ink);font-size:5.5px;align-items:flex-end;padding-bottom:2px}
.fax-row span{width:172px}
.fax-checks{position:absolute;left:12px;top:241px;display:flex;gap:13px;font-size:5.5px}
.fax-checks span{display:flex;align-items:center;gap:4px}
.fax-checks i{display:inline-block;width:7px;height:7px;border:1px solid var(--ink)}

/* envelopes */
.envelope-back{left:797px;top:20px;width:350px;height:150px;background:var(--paper-shade)}
.envelope-mid{left:785px;top:92px;width:351px;height:150px;background:var(--paper-shade)}
.envelope-front{left:760px;top:174px;width:379px;height:164px;background:linear-gradient(180deg,#fff 40%,#ececec)}
.flap{position:absolute;left:0;top:0}
.env-foot{position:absolute;bottom:5px;font-size:6.5px;color:var(--ink)}

/* cards */
.card{top:366px;height:76px}
.card-light{left:731px;width:139px}
.card-dark{left:880px;width:141px;background:var(--card-dark)}
.card-grey{left:1026px;width:139px;background:var(--card-grey)}
.card-centered{display:flex;flex-direction:column;align-items:center;justify-content:center;gap:6px}
.card-web{font-size:6.5px;color:var(--paper)}
.card-name{position:absolute;right:6px;top:8px;font-size:6px;color:var(--paper);line-height:7px;text-align:right}
.card-details{position:absolute;left:5px;bottom:6px;display:flex;gap:6px;font-size:4px;line-height:5px}

.option-label{position:absolute;color:var(--label);font-size:25px}
</style>
</head>
<body>

<!-- Letterhead, option 1 -->
<section class="sheet letterhead-a" aria-label="Letterhead option 1">
  <svg class="swoop" width="338" height="200" viewBox="0 0 338 200">
    <path d="M90 0 C210 14 318 70 338 200 L338 0 Z" fill="var(--swoop-grey)"/>
    <path d="M110 0 C220 12 316 60 338 170 L338 0 Z" fill="var(--brand-blue)"/>
  </svg>
  <div class="brand" style="left:10px;top:50px;font-size:18px"><span class="brand-dot" style="width:14px;height:14px"></span>Halvora</div>
  <p class="header-address" style="left:236px;top:26px">Street Name, City Name<br>State Zipcode</p>
  <ul class="contact-list" style="left:10px;top:388px">
    <li><svg viewBox="0 0 10 10"><path d="M2 0h2l1 3-1.5 1a6 6 0 0 0 2.5 2.5L7 5l3 1v2c0 1-1 2-2 2A8 8 0 0 1 0 2c0-1 1-2 2-2z"/></svg>123-456-7890</li>
    <li><svg viewBox="0 0 10 10"><path d="M2 0h2l1 3-1.5 1a6 6 0 0 0 2.5 2.5L7 5l3 1v2c0 1-1 2-2 2A8 8 0 0 1 0 2c0-1 1-2 2-2z"/></svg>123-456-7856</li>
    <li><svg viewBox="0 0 10 10"><rect x="0" y="2" width="10" height="6"/></svg>hello@halvora-mail.com</li>
    <li><svg viewBox="0 0 10 10"><circle cx="5" cy="5" r="5"/></svg>www.halvora.com</li>
  </ul>
</section>

<!-- Letterhead, option 2 (fax) -->
<section class="sheet letterhead-b" aria-label="Fax sheet option 2">
  <svg class="swoop" width="339" height="200" viewBox="0 0 339 200">
    <path d="M90 0 C210 14 318 70 339 200 L339 0 Z" fill="var(--swoop-grey)"/>
    <path d="M110 0 C220 12 316 60 339 170 L339 0 Z" fill="var(--brand-blue)"/>
  </svg>
  <div class="brand" style="left:10px;top:50px;font-size:18px"><span class="brand-dot" style="width:14px;height:14px"></span>Halvora</div>
  <p class="header-address" style="left:236px;top:26px">Street Name, City Name<br>State Zipcode</p>
  <h1 class="fax-title">FAX</h1>
  <div class="fax-fields">
    <div class="fax-row"><span>To :</span>From :</div>
    <div class="fax-row"><span>Fax :</span>Pages :</div>
    <div class="fax-row"><span>Phone :</span>Date :</div>
    <div class="fax-row"><span>Re :</span>CC :</div>
  </div>
  <div class="fax-checks">
    <span><i></i>Urgent</span><span><i></i>For Review</span><span><i></i>Please Comment</span><span><i></i>Please Reply</span><span><i></i>Please Recycle</span>
  </div>
  <ul class="contact-list" style="left:10px;top:388px">
    <li><svg viewBox="0 0 10 10"><path d="M2 0h2l1 3-1.5 1a6 6 0 0 0 2.5 2.5L7 5l3 1v2c0 1-1 2-2 2A8 8 0 0 1 0 2c0-1 1-2 2-2z"/></svg>123-456-7890</li>
    <li><svg viewBox="0 0 10 10"><path d="M2 0h2l1 3-1.5 1a6 6 0 0 0 2.5 2.5L7 5l3 1v2c0 1-1 2-2 2A8 8 0 0 1 0 2c0-1 1-2 2-2z"/></svg>123-456-7856</li>
    <li><svg viewBox="0 0 10 10"><rect x="0" y="2" width="10" height="6"/></svg>hello@halvora-mail.com</li>
    <li><svg viewBox="0 0 10 10"><circle cx="5" cy="5" r="5"/></svg>www.halvora.com</li>
  </ul>
</section>

<!-- Envelopes -->
<section class="sheet envelope-back" aria-label="Envelope back, grey flap">
  <svg class="flap" width="350" height="70" viewBox="0 0 350 70"><path d="M0 0H350V8L200 64Q175 70 150 64L0 8Z" fill="var(--swoop-grey)"/></svg>
</section>
<section class="sheet envelope-mid" aria-label="Envelope back, blue flap">
  <svg class="flap" width="351" height="70" viewBox="0 0 351 70"><path d="M0 0H351V10L200 62Q175 68 150 62L0 10Z" fill="var(--brand-blue)"/></svg>
</section>
<section class="sheet envelope-front" aria-label="Envelope front">
  <svg class="swoop" width="379" height="110" viewBox="0 0 379 110">
    <path d="M120 0 C250 6 350 40 379 110 L379 0 Z" fill="var(--swoop-grey)"/>
    <path d="M140 0 C260 4 352 30 379 84 L379 0 Z" fill="var(--brand-blue)"/>
  </svg>
  <div class="brand" style="left:12px;top:44px;font-size:18px"><span class="brand-dot" style="width:14px;height:14px"></span>Halvora</div>
  <p class="env-foot" style="left:10px">Street Name, City Name; State Zipcode</p>
  <p class="env-foot" style="right:10px">www.<b>halvora</b>.com</p>
</section>

<!-- Business cards -->
<section class="sheet card card-light" aria-label="Business card front">
  <svg class="swoop" width="139" height="60" viewBox="0 0 139 60">
    <path d="M30 0 C90 4 130 24 139 60 L139 0 Z" fill="var(--swoop-grey)"/>
    <path d="M40 0 C95 3 130 18 139 48 L139 0 Z" fill="var(--brand-blue)"/>
  </svg>
  <p class="card-name">Your Name<br>Title</p>
  <div class="brand" style="left:6px;top:12px;font-size:10px;gap:3px"><span class="brand-dot" style="width:7px;height:7px"></span>Halvora</div>
  <div class="card-details">
    <p>123-456-7890<br>123-456-7856<br>hello@halvora-mail.com<br>www.halvora.com</p>
    <p>Street Name, City Name<br>State Zipcode</p>
  </div>
</section>
<section class="sheet card card-dark card-centered" aria-label="Business card back, dark">
  <div class="brand" style="position:static;font-size:15px"><span class="brand-dot" style="width:11px;height:11px"></span>Halvora</div>
  <p class="card-web">www.halvora.com</p>
</section>
<section class="sheet card card-grey card-centered" aria-label="Business card back, grey">
  <div class="brand" style="position:static;font-size:15px"><span class="brand-dot" style="width:11px;height:11px"></span>Halvora</div>
  <p class="card-web">www.halvora.com</p>
</section>

<p class="option-label" style="left:127px;top:455px">Option-1</p>
<p class="option-label" style="left:482px;top:462px">Option-2</p>

</body>
</html>
```